Visitenkarten-Design für Rohrreinigungsfirma
Zielgruppe
Wir sind eine Kanal.-Rohrreinigungsfirma und suchen ein hochwertiges Design, unsere Zielgruppe sind Firmenkunden,Hausverwaltungen, Architekten sowie Behörden.
Aufgabenstellung
Das Design sollte Edel aussehen. Es sollten unsere Dienstleistungen mit auf der Visitenkarte stehen (gerne auch Rückseite): grabenlose Kanalsanierung, TV-Kamerainspektion,Dichtheitsprüfung DIN EN 1610, Fräsarbeiten mit Roboter, Fräsarbeiten mit Wasserhöchstdruck 2.500 Bar,Verstopfungsbeseitigung. (Vorderseite sollte enthalten:

```html
<!DOCTYPE html>
<html lang="de">
<head>
<meta charset="utf-8">
<title>Visitenkarte KRB Kanal- &amp; Rohrreinigung</title>
<link rel="stylesheet" href="https://fonts.googleapis.com/css2?family=Montserrat:wght@500;600;700;800&display=swap">
<style>
  :root {
    --blue: #3a5d82;
    --navy: #2b3a52;
    --red: #b01e23;
    --ink: #2e3a4f;
    --white: #ffffff;
    --page: #ffffff;
  }
  * { margin: 0; padding: 0; box-sizing: border-box; }
  html, body { width: 995px; height: 1200px; overflow: hidden; background: var(--page); }
  body { position: relative; font-family: "Montserrat", Arial, sans-serif; color: var(--ink); }

  .side-title {
    position: absolute; left: 0; width: 936px; text-align: center;
    font-size: 29px; font-weight: 700; color: var(--ink);
  }
  .side-title--front { top: 88px; }
  .side-title--back { top: 636px; }

  .card {
    position: absolute; left: 199px; width: 527px; height: 341px;
    background: var(--white); overflow: hidden;
    box-shadow: 0 2px 6px rgba(0,0,0,0.25);
  }
  .card--front { top: 175px; }
  .card--back { top: 718px; }
  .card__bg { position: absolute; inset: 0; }

  .benefits { position: absolute; left: 26px; top: 36px; list-style: none; color: var(--white); font-size: 13px; font-weight: 600; line-height: 17px; }
  .benefits li { position: relative; padding-left: 20px; margin-bottom: 8px; }
  .benefits li::before { content: "✓"; position: absolute; left: 0; top: -1px; font-size: 15px; font-weight: 700; }

  .hotline { position: absolute; color: var(--white); font-weight: 700; text-align: center; }
  .card--front .hotline { left: 10px; top: 242px; width: 190px; font-size: 16.5px; line-height: 23px; }
  .card--back .hotline { left: 8px; top: 250px; width: 170px; font-size: 15px; line-height: 20px; }

  .brand { position: absolute; left: 240px; top: 18px; display: flex; align-items: center; gap: 10px; }
  .brand__name { font-size: 46px; font-weight: 800; color: var(--blue); letter-spacing: 1px; line-height: 50px; }
  .brand__dot { width: 26px; height: 26px; border-radius: 50%; background: var(--blue); }
  .brand__claim { position: absolute; left: 240px; top: 72px; font-size: 16.5px; font-weight: 700; color: var(--navy); }
  .brand__service { position: absolute; left: 288px; top: 94px; font-size: 11px; font-weight: 600; color: var(--red); }

  .contact { position: absolute; left: 294px; color: var(--blue); font-weight: 600; font-size: 15.5px; }
  .contact--name { top: 122px; line-height: 24px; }
  .contact--phone { top: 177px; display: flex; align-items: center; gap: 6px; }
  .contact--address { top: 208px; line-height: 24px; }
  .band-text { position: absolute; right: 28px; color: var(--white); font-weight: 500; font-size: 15.5px; }
  .card--front .band-text { top: 284px; }
  .card--back .band-text { top: 288px; font-size: 15px; }

  .services { position: absolute; left: 24px; top: 24px; list-style: none; color: var(--white); font-size: 15px; font-weight: 500; line-height: 19px; }
  .services li { position: relative; padding-left: 16px; margin-bottom: 11.5px; }
  .services li::before { content: ""; position: absolute; left: 1px; top: 8px; width: 5px; height: 5px; border-radius: 50%; background: var(--white); }

  .callout { position: absolute; left: 328px; top: 58px; width: 190px; text-align: center; font-size: 18.5px; font-weight: 700; line-height: 25px; color: var(--ink); }
  .callout p + p { margin-top: 25px; }
</style>
</head>
<body>

<h2 class="side-title side-title--front">Vorderseite</h2>
<section class="card card--front">
  <svg class="card__bg" width="527" height="341" viewBox="0 0 527 341">
    <polygon points="0,0 173,0 302,341 0,341" fill="var(--blue)"/>
    <rect x="240" y="270" width="287" height="49" fill="var(--navy)"/>
    <polygon points="0,270 285,270 302,319 302,341 0,341" fill="var(--blue)"/>
    <path d="M0,236 H230 A38.5,38.5 0 0 1 230,313 H0 Z" fill="var(--red)"/>
    <g fill="none" stroke="var(--white)" stroke-width="3">
      <circle cx="234" cy="273" r="22"/>
      <polyline points="234,260 234,274 243,280"/>
    </g>
    <g fill="var(--white)">
      <rect x="193" y="280" width="22" height="16"/>
      <path d="M215,284 h8 l5,6 v6 h-13 z"/>
      <circle cx="199" cy="298" r="3.5" stroke="var(--red)" stroke-width="1.5"/>
      <circle cx="221" cy="298" r="3.5" stroke="var(--red)" stroke-width="1.5"/>
    </g>
  </svg>
  <ul class="benefits">
    <li>transparente<br>Preise</li>
    <li>moderne<br>Ausrüstung</li>
    <li>regionales<br>Unternehmen</li>
    <li>schnell &amp; zuverlässiger<br>Service</li>
  </ul>
  <div class="hotline">24H NOTDIENST<br>Tag &amp; Nacht<br>0151 - 000 111 22</div>

  <div class="brand"><span class="brand__name">KRB</span><span class="brand__dot"></span></div>
  <div class="brand__claim">KANAL- &amp; ROHRREINIGUNG</div>
  <div class="brand__service">24 STUNDEN NOTDIENST</div>

  <div class="contact contact--name">JONAS BERGER<br>Geschäftsführer</div>
  <div class="contact contact--phone">
    <svg width="13" height="13" viewBox="0 0 24 24"><path fill="var(--blue)" d="M6.6 10.8a15.1 15.1 0 0 0 6.6 6.6l2.2-2.2a1 1 0 0 1 1-.25 11.4 11.4 0 0 0 3.6.57 1 1 0 0 1 1 1V20a1 1 0 0 1-1 1A17 17 0 0 1 3 4a1 1 0 0 1 1-1h3.5a1 1 0 0 1 1 1c0 1.25.2 2.45.57 3.57a1 1 0 0 1-.25 1z"/></svg>
    07000 - 123 45 67
  </div>
  <div class="contact contact--address">Lindenweg 14<br>73999 Musterbach/Talheim</div>
  <div class="band-text">info@rohrreinigung-krb.de</div>
</section>

<h2 class="side-title side-title--back">Rückseite</h2>
<section class="card card--back">
  <svg class="card__bg" width="527" height="341" viewBox="0 0 527 341">
    <polygon points="0,0 269,0 398,341 0,341" fill="var(--blue)"/>
    <rect x="230" y="271" width="297" height="53" fill="var(--navy)"/>
    <path d="M0,245 H213 A33.5,33.5 0 0 1 213,312 H0 Z" fill="var(--red)"/>
    <g fill="none" stroke="var(--white)" stroke-width="3">
      <circle cx="216" cy="276" r="19"/>
      <polyline points="216,265 216,277 224,282"/>
    </g>
    <g fill="var(--white)">
      <rect x="180" y="283" width="19" height="14"/>
      <path d="M199,286 h7 l4,5 v6 h-11 z"/>
      <circle cx="185" cy="299" r="3" stroke="var(--red)" stroke-width="1.5"/>
      <circle cx="204" cy="299" r="3" stroke="var(--red)" stroke-width="1.5"/>
    </g>
  </svg>
  <ul class="services">
    <li>grabenlose Kanalsanierung</li>
    <li>TV-Kamerainspektion</li>
    <li>Dichtheitsprüfung DIN EN 1610</li>
    <li>Fräsarbeiten mit Roboter</li>
    <li>Fräsarbeiten mit<br>Wasserhöchstdruck 2.500 Bar</li>
    <li>Verstopfungsbeseitigung</li>
  </ul>
  <div class="hotline">24H NOTDIENST<br>Tag &amp; Nacht<br>0151 - 000 111 22</div>
  <div class="callout">
    <p>Abfluss oder<br>Rohr verstopft?</p>
    <p>Jetzt anrufen,<br>wir kommen<br>sofort!</p>
  </div>
  <div class="band-text">www.rohrreinigung-krb.de</div>
</section>

</body>
</html>
```